Medical Services company. Need a website that blows the competition out of the water

We need a web site designed to draw attention to our many services offered. We are a Medical Services business based out of Pennsylvania. We provide basic first aid staffing for events and businesses such as but not limited to: Fairs, Festivals, Carnivals, Sporting events, Large gatherings where a first aid station is needed, Concerts, Businesses with first aid needs . We provide training and certifications that are tailored to the customers needs. We provide Covid-19 pre screening and temperature monitoring. Our professionals consist of individuals with Basic First Aid, Certified Nursing Assistants, Medical Assistants, Emergency Medical Responders (EMR), Emergency Medical Technicians (EMT), and Nurses. I do not know how many pages I will need since we offer multiple different services. Our main services provided are: First Aid services, Covid-19 pre screen and temperatures, and Training/Certifications. You will have to use stock photos for now until I can get some actual photographs of our team.I have uploaded a copy of my brochure so you can get some information from there as well.

Target Market(s)

-For the first Aid and Covid-19 services: All Businesses, Sporting events, Event organizers
-Training: Everyone.

Coding

Number of Pages Required

Font styles to use
Sans Serif

Requirements
Must have
• My colors are what is in the logos and Gray , need to have a way for customers to request a quote, design that grabs their attention. Should have pictures of medical providers attending to the sick or injured. Both in a office setting and in an emergency out in public. Should have pictures of an ambulance. Should also have pictures of staff taking temperatures and asking pre screening questions.
Nice to have
• I'll get back to you on that one

```html
<!DOCTYPE html>
<html lang="en">
<head>
<meta charset="utf-8">
<title>Vantera Medical Services</title>
<link rel="stylesheet" href="https://fonts.googleapis.com/css2?family=Poppins:wght@300;400;500;600;700;800&family=Noto+Serif:wght@400&display=swap">
<style>
:root{
  --green:#05c796;
  --blue:#0a0399;
  --gray:#ececec;
  --ink:#111;
  --muted:#555;
  --white:#fff;
}
*{box-sizing:border-box;margin:0;padding:0}
html,body{width:1200px;height:2962px;overflow:hidden}
body{position:relative;font-family:"Poppins",sans-serif;color:var(--ink);background:var(--white)}
.abs{position:absolute}
a{color:inherit;text-decoration:none}

/* hero */
.gray-band{left:0;top:598px;width:1200px;height:443px;background:var(--gray);clip-path:polygon(0 0,100% 0,100% 100%,0 357px)}
.hero-photo{left:0;top:0;width:1200px;height:690px;z-index:1;
  background:linear-gradient(100deg,#3b3f44 0%,#6b7075 40%,#9a9fa4 65%,#7d7f83 100%);
  clip-path:polygon(0 0,100% 0,100% 690px,0 598px)}
.brand{left:62px;top:14px;display:flex;align-items:center;gap:10px;color:var(--white);font-weight:700;font-size:40px;letter-spacing:1px;line-height:1;z-index:2}
.brand .dot{width:60px;height:60px;border-radius:50%;background:var(--white)}
.brand small{display:block;font-size:13px;font-weight:700;letter-spacing:1px;margin-top:2px}
.nav{right:60px;top:32px;display:flex;gap:32px;font-size:12px;color:var(--white);align-items:center;z-index:2}
.nav .active{color:var(--green)}
.nav .active::before{content:"";display:inline-block;border:5px solid transparent;border-top:7px solid var(--green);margin-right:4px;vertical-align:-2px}
.hero-title{left:62px;top:285px;color:var(--white);font-weight:800;font-size:39px;line-height:50px;text-shadow:0 2px 4px rgba(0,0,0,.45);z-index:2}
.btn{display:inline-block;background:var(--green);color:var(--white);font-weight:600;border-radius:20px;text-align:center}
.hero-btn{left:60px;top:393px;width:150px;height:38px;line-height:38px;font-size:15px;z-index:2}

/* sections */
.heading{font-weight:600;font-size:34px;border-left:3px solid var(--green);padding-left:10px;line-height:60px}
.services-head{left:60px;top:680px}
.service{width:260px;text-align:center}
.service .ring{width:116px;height:116px;border-radius:50%;background:var(--green);border:3px solid var(--blue);margin:0 auto;display:flex;align-items:center;justify-content:center}
.service h3{font-family:"Noto Serif",serif;font-weight:400;font-size:21px;margin-top:10px}
.service .more{font-size:12px;font-weight:700;color:var(--blue)}
.service .more::after{content:"";display:inline-block;border:5px solid transparent;border-left:6px solid var(--blue);border-right:0;margin-left:5px;vertical-align:-1px}

.about-photo{left:129px;top:1056px;width:414px;height:414px;border-radius:50%;background:radial-gradient(circle at 55% 45%,#8fb0e0,#3d5fa8 70%,#1c2f63)}
.about-inset{left:146px;top:1070px;width:164px;height:164px;border-radius:50%;border:12px solid var(--white);background:linear-gradient(135deg,#c9c3be,#8c8782)}
.about-badge{left:424px;top:1346px;width:130px;height:130px;border-radius:50%;border:12px solid var(--white);background:var(--green)}
.about-head{left:645px;top:1106px}
.about-text{left:646px;top:1174px;width:530px;font-size:12.4px;color:var(--muted);line-height:19.5px}
.about-text p{margin-bottom:10.5px}
.about-btn{left:645px;top:1424px;width:150px;height:38px;line-height:38px;font-size:15px}

.help{left:0;top:1545px;width:1200px;height:241px;background:var(--blue);color:var(--white);text-align:center}
.help h2{font-weight:600;font-size:30px;margin-top:42px}
.help .sub{font-size:12.5px;margin-top:2px}
.help .call{display:flex;justify-content:center;align-items:center;gap:16px;margin-top:8px;font-size:20px;font-weight:500}
.help .call .num{font-size:24px;letter-spacing:1px}
.help .phone{width:46px;height:46px;border-radius:50%;background:var(--white);display:flex;align-items:center;justify-content:center}
.help .mail{display:inline-block;margin-top:12px;font-size:13px;text-decoration:underline}

.testi-head{left:512px;top:1844px}
.card{width:424px}
.card .bar{height:2px;background:var(--blue);margin-top:0}
.card .quote{position:absolute;left:24px;top:-30px;background:var(--white);padding:0 6px;color:var(--green);font-size:64px;font-weight:700;line-height:60px;font-family:Georgia,serif}
.card .box{background:#efefef;height:124px;padding:38px 26px 0;font-size:12.4px;line-height:19.5px;color:#777}
.card .who{display:flex;align-items:center;gap:14px;margin:20px 0 0 24px;font-size:13px}
.card .avatar{width:52px;height:52px;border-radius:50%;background:linear-gradient(135deg,#9a8a80,#4a3f3a)}
.card .name{color:var(--blue)}
.card .role{color:#666}

.contact-band{left:0;top:2169px;width:1200px;height:400px;background:var(--gray);clip-path:polygon(0 88px,100% 0,100% 100%,0 100%)}
.contact-head{left:484px;top:2258px}
.field{background:var(--white);border:1px solid #ccc;border-radius:3px;font-size:12px;color:#555;padding:10px 8px}
.field.focus{border-color:var(--blue)}
.submit{left:548px;top:2515px;width:104px;height:37px;line-height:37px;font-size:15px}

.footer{left:0;top:2550px;width:1200px;height:412px;background:var(--blue);clip-path:polygon(0 92px,100% 0,100% 100%,0 100%);color:var(--white)}
.foot-brand{left:62px;top:2684px;font-size:36px}
.foot-brand .dot{width:52px;height:52px}
.foot-brand small{font-size:11px}
.foot-about{left:62px;top:2752px;width:240px;font-size:12.4px;line-height:19.5px}
.foot-col h4{font-size:18px;font-weight:500;margin-bottom:8px}
.foot-col li{list-style:none;font-size:12.4px;line-height:30px}
.loc{display:flex;gap:14px;font-size:12.4px;line-height:19px;margin-top:14px}
.news-input{left:889px;top:2720px;width:253px;height:37px;background:var(--white);color:#555;font-size:12px;padding:10px 8px}
.news-btn{left:889px;top:2769px;width:253px;height:37px;line-height:37px;background:var(--green);color:var(--white);text-align:center;font-size:15px;font-weight:500}
.socials{left:889px;top:2819px;display:flex;gap:5px}
.socials span{width:26px;height:26px;border-radius:50%;border:1px solid var(--white);display:block}
.socials span:first-child{background:#1da1f2;border-color:#1da1f2}
.copy{left:0;top:2927px;width:1200px;height:35px;background:var(--green);color:var(--white);text-align:center;font-size:12px;line-height:35px}
</style>
</head>
<body>

<div class="abs gray-band"></div>
<div class="abs hero-photo" role="img" aria-label="Smiling doctor in a white coat with a stethoscope, clinic staff in the background"></div>
<div class="abs brand"><span class="dot"></span><div>VANTERA<small>Medical Services</small></div></div>
<nav class="abs nav">
  <a class="active">HOME</a><a>ABOUT US</a><a>SERVICES</a><a>REQUEST A QUOTE</a><a>CONTACT US</a>
  <svg width="16" height="16" viewBox="0 0 16 16" fill="none" stroke="#fff" stroke-width="1.6"><circle cx="6.5" cy="6.5" r="5"/><path d="M10 10l5 5"/></svg>
</nav>
<h1 class="abs hero-title">PROVIDING ALL OF YOUR HEALTH<br>AND SAFETY NEEDS</h1>
<a class="abs btn hero-btn">CONTACT US</a>

<h2 class="abs heading services-head">Our Services</h2>

<div class="abs service" style="left:56px;top:747px">
  <div class="ring"><svg width="54" height="54" viewBox="0 0 54 54" fill="none" stroke="#fff" stroke-width="2.4"><rect x="6" y="15" width="42" height="30" rx="5"/><path d="M20 15v-5h14v5M23 24h8v5h5v8h-5v5h-8v-5h-5v-8h5z"/></svg></div>
  <h3>First Aid</h3><a class="more">READ MORE</a>
</div>
<div class="abs service" style="left:332px;top:747px">
  <div class="ring"><svg width="54" height="54" viewBox="0 0 54 54" fill="none" stroke="#fff" stroke-width="2.4"><path d="M27 5l15 6v11c0 9-7 14-15 17-8-3-15-8-15-17V11z"/><path d="M24 14h6v5h5v6h-5v5h-6v-5h-5v-6h5z"/><path d="M6 34l8 8h10M48 34l-8 8H30"/></svg></div>
  <h3>Onsite Care</h3><a class="more">READ MORE</a>
</div>
<div class="abs service" style="left:607px;top:747px">
  <div class="ring"><svg width="56" height="52" viewBox="0 0 56 52" fill="none" stroke="#fff" stroke-width="2.4"><path d="M28 48L7 27C0 20 3 6 15 5c6 0 10 4 13 8 3-4 7-8 13-8 12 1 15 15 8 22z"/><path d="M8 24h12l3-6 4 12 4-9 3 5h14"/></svg></div>
  <h3>Resuscita</h3><a class="more">READ MORE</a>
</div>
<div class="abs service" style="left:883px;top:747px">
  <div class="ring"><svg width="56" height="56" viewBox="0 0 56 56" fill="none" stroke="#fff" stroke-width="2.2"><circle cx="28" cy="28" r="14"/><circle cx="24" cy="25" r="2.5"/><circle cx="32" cy="30" r="2.5"/><circle cx="27" cy="34" r="2"/><path d="M28 6v8M28 42v8M6 28h8M42 28h8M12 12l6 6M38 38l6 6M44 12l-6 6M18 38l-6 6"/></svg></div>
  <h3>Covid-19 Pre Screening</h3><a class="more">READ MORE</a>
</div>

<div class="abs about-photo" role="img" aria-label="Surgical team in caps and masks looking down over a patient"></div>
<div class="abs about-inset" role="img" aria-label="Doctor with a clipboard talking to a patient"></div>
<div class="abs about-badge"></div>
<h2 class="abs heading about-head">About Us</h2>
<div class="abs about-text">
  <p>you will notice the dif erence when you choose Vantera for your business event.</p>
  <p>By having trained,profassional,responders presenr,your staf will feel safer and morale will &nbsp;improve,productivity will increase and incidents will reduce.</p>
  <p>Our goal is to provide the best care and coverage to uor cusomers patients.</p>
  <p>We are passionate about people and will straive to keep everyone healthy and saff.</p>
  <p>you will notice the dif erence when you choose Vantera for your business event.</p>
  <p>By having trained,profassional,responders presenr,your staf will feel safer and morale will &nbsp;improve,productivity will increase and incidents will reduce.</p>
  <p>Our goal is to provide the best care and coverage to uor cusomers patients.</p>
</div>
<a class="abs btn about-btn">LEARN MORE</a>

<section class="abs help">
  <h2>Vantera Medical Services Is Here To Help You</h2>
  <p class="sub">Lorem Ipsum is simply dummy text of the printing and typesetting industry. Lorem Ipsum has been the industry's</p>
  <div class="call">CALL US TODAY :
    <span class="phone"><svg width="24" height="24" viewBox="0 0 24 24"><path fill="#05c796" d="M6.6 10.8c1.4 2.8 3.8 5.1 6.6 6.6l2.2-2.2c.3-.3.7-.4 1-.2 1.1.4 2.3.6 3.6.6.6 0 1 .4 1 1V20c0 .6-.4 1-1 1C10.6 21 3 13.4 3 4c0-.6.4-1 1-1h3.5c.6 0 1 .4 1 1 0 1.3.2 2.5.6 3.6.1.3 0 .7-.2 1z"/></svg></span>
    <span class="num">555 014 2286</span></div>
  <a class="mail">info@vanteramedical.com</a>
</section>

<h2 class="abs heading testi-head">Testimonials</h2>
<div class="abs card" style="left:161px;top:1933px">
  <div class="bar"></div><span class="quote">“</span>
  <div class="box">Lorem Ipsum is simply dummy text of the printing and typesetting industry. Lorem Ipsum has been the industry's standard dummy text ever since the 1500s, when an unknown printer took a galley.</div>
  <div class="who"><span class="avatar" role="img" aria-label="Client portrait"></span><div><div class="name">Client Name</div><div class="role">Lorem Ipsum</div></div></div>
</div>
<div class="abs card" style="left:615px;top:1933px">
  <div class="bar"></div><span class="quote">“</span>
  <div class="box">Lorem Ipsum is simply dummy text of the printing and typesetting industry. Lorem Ipsum has been the industry's standard dummy text ever since the 1500s, when an unknown printer took a galley.</div>
  <div class="who"><span class="avatar" role="img" aria-label="Client portrait"></span><div><div class="name">Client Name</div><div class="role">Lorem Ipsum</div></div></div>
</div>

<div class="abs contact-band"></div>
<h2 class="abs heading contact-head">Get In Touch</h2>
<div class="abs field focus" style="left:267px;top:2338px;width:322px;height:37px">Name :</div>
<div class="abs field" style="left:611px;top:2338px;width:322px;height:37px">Email :</div>
<div class="abs field" style="left:267px;top:2385px;width:322px;height:37px">Phone no :</div>
<div class="abs field" style="left:611px;top:2385px;width:322px;height:37px">Address :</div>
<div class="abs field" style="left:267px;top:2434px;width:666px;height:67px">Massage :</div>
<a class="abs btn submit">SUBMIT</a>

<footer class="abs footer"></footer>
<div class="abs brand foot-brand"><span class="dot"></span><div>VANTERA<small>Medical Services</small></div></div>
<p class="abs foot-about" style="color:#fff">" Lorem Ipsum is simply dummy text of the printing and typesetting industry. Lorem Ipsum has been the industry's standard dummy text ever since the an unknown printer took a galley of type and</p>
<div class="abs foot-col" style="left:339px;top:2680px;color:#fff">
  <h4>Use Full Links</h4>
  <ul><li>- Home</li><li>- About Us</li><li>- Services</li><li>- Requaste A QUote</li><li>-Contact us</li></ul>
</div>
<div class="abs foot-col" style="left:614px;top:2680px;color:#fff;width:230px">
  <h4>Location</h4>
  <div class="loc"><svg width="18" height="22" viewBox="0 0 18 22"><path fill="#fff" d="M9 0a8 8 0 018 8c0 6-8 14-8 14S1 14 1 8a8 8 0 018-8zm0 5a3 3 0 100 6 3 3 0 000-6z"/></svg><span>Lorem Ipsum is simply dummy text of the printing and ,</span></div>
  <div class="loc" style="margin-top:22px"><svg width="18" height="18" viewBox="0 0 24 24"><path fill="#fff" d="M6.6 10.8c1.4 2.8 3.8 5.1 6.6 6.6l2.2-2.2c.3-.3.7-.4 1-.2 1.1.4 2.3.6 3.6.6.6 0 1 .4 1 1V20c0 .6-.4 1-1 1C10.6 21 3 13.4 3 4c0-.6.4-1 1-1h3.5c.6 0 1 .4 1 1 0 1.3.2 2.5.6 3.6.1.3 0 .7-.2 1z"/></svg><span>Phone<br>555.014.2286</span></div>
  <div class="loc" style="margin-top:22px"><svg width="18" height="18" viewBox="0 0 20 20" fill="none" stroke="#fff" stroke-width="1.4"><circle cx="10" cy="10" r="8.5"/><ellipse cx="10" cy="10" rx="4" ry="8.5"/><path d="M1.5 10h17M3 5.5h14M3 14.5h14"/></svg><span>Globle<br>www.vanteramedical.com</span></div>
</div>
<div class="abs foot-col" style="left:890px;top:2680px;color:#fff"><h4>News Letters</h4></div>
<div class="abs news-input">Enter Email....</div>
<div class="abs news-btn">SUBMIT</div>
<div class="abs socials"><span></span><span></span><span></span><span></span></div>
<div class="abs copy">©Vantera medical Services2020-ALL RIGHT RESERVED</div>

</body>
</html>
```